Design for Chirpwall Ad to promote Laptops purchase

Need a graphic design for a Chirpwall Ad - to promote 2 laptops (PC and Zorvane) with the stated required ad-text.

AD TEXT:

FOR SME BUSINESS ONLY!
Chat with us!
To get advice on how to apply
and defray up to 80%* of business laptop purchase cost!

*Terms and Conditions apply

Image for reference only

Target Market(s)

Small medium business

Font styles to use
Sans Serif

Requirements
Must have
• 2 laptop images (see attached ) - 1 vector image of ZORVANE , and pls try to create another vector image of PC laptop (where screen is showing Blue Pendrel screen)

```html
<!DOCTYPE html>
<html lang="en">
<head>
<meta charset="utf-8">
<title>For SME Business Only – Laptop Ad</title>
<link href="https://fonts.googleapis.com/css2?family=Anton&family=Bebas+Neue&family=Rubik:wght@400&display=swap" rel="stylesheet">
<style>
  :root {
    --red: #e8000b;
    --red-deep: #b8000a;
    --red-bright: #ff1a1a;
    --white: #ffffff;
    --ink: #111111;
    --pink: #f59ab5;
    --dot-red: #f0323c;
  }
  html, body {
    margin: 0;
    padding: 0;
    width: 1200px;
    height: 754px;
    overflow: hidden;
    background: var(--white);
  }
  .ad {
    position: relative;
    width: 1200px;
    height: 754px;
    overflow: hidden;
    font-family: "Rubik", sans-serif;
  }
  .ad-backdrop {
    position: absolute;
    inset: 0;
  }
  .laptop {
    position: absolute;
    border-radius: 10px;
  }
  .laptop-zorvane {
    left: 43px; top: 40px; width: 420px; height: 270px;
    background: linear-gradient(160deg, #d9dadd 0%, #c96fc8 35%, #5b3a8e 70%, #b9bcc2 100%);
  }
  .laptop-pc {
    left: 118px; top: 358px; width: 375px; height: 342px;
    background: linear-gradient(170deg, #1a3fd0 0%, #0a2aa8 55%, #c9ccd1 78%, #e3e5e8 100%);
  }
  .headline {
    position: absolute;
    right: 87px;
    top: 116px;
    margin: 0;
    font-family: "Anton", sans-serif;
    font-weight: 400;
    font-size: 76px;
    line-height: 1;
    letter-spacing: -1px;
    color: var(--white);
    -webkit-text-stroke: 3px var(--ink);
    paint-order: stroke fill;
    white-space: nowrap;
  }
  .cta {
    position: absolute;
    left: 870px;
    top: 265px;
    width: 243px;
    height: 76px;
    border-radius: 10px;
    background: var(--red);
    box-shadow: 0 4px 0 var(--red-deep);
    color: var(--white);
    font-family: "Bebas Neue", sans-serif;
    font-size: 50px;
    line-height: 78px;
    text-align: center;
    letter-spacing: 0.5px;
  }
  .offer {
    position: absolute;
    right: 87px;
    top: 394px;
    margin: 0;
    text-align: right;
    font-size: 29px;
    line-height: 62px;
    letter-spacing: 1px;
    color: var(--ink);
  }
  .offer .highlight { color: var(--red); }
  .terms {
    position: absolute;
    right: 87px;
    top: 609px;
    margin: 0;
    font-size: 17px;
    letter-spacing: 0.3px;
    color: var(--red);
  }
</style>
</head>
<body>
<main class="ad">
  <svg class="ad-backdrop" width="1200" height="754" viewBox="0 0 1200 754" aria-hidden="true">
    <defs>
      <linearGradient id="redPanel" x1="0" y1="0" x2="1" y2="1">
        <stop offset="0" stop-color="#d8000a"/>
        <stop offset="0.5" stop-color="#c4000a"/>
        <stop offset="1" stop-color="#f40010"/>
      </linearGradient>
    </defs>
    <polygon points="0,0 985,0 360,754 0,754" fill="url(#redPanel)"/>
    <g stroke="#a80008" stroke-width="10" stroke-linecap="round" opacity="0.6">
      <line x1="680" y1="50" x2="380" y2="440"/>
      <line x1="560" y1="90" x2="330" y2="380"/>
    </g>
    <g stroke="#ffffff" stroke-width="8" stroke-linecap="round">
      <line x1="236" y1="19" x2="16" y2="288"/>
      <line x1="453" y1="78" x2="203" y2="370"/>
      <line x1="633" y1="313" x2="286" y2="727"/>
      <line x1="118" y1="478" x2="21" y2="594"/>
    </g>
  </svg>

  <div class="laptop laptop-zorvane" role="img" aria-label="Zorvane laptop, open, with a purple and pink space wallpaper"></div>
  <div class="laptop laptop-pc" role="img" aria-label="PC laptop, open, showing a blue Pendrel start screen"></div>

  <svg class="ad-backdrop" width="1200" height="754" viewBox="0 0 1200 754" aria-hidden="true">
    <polygon points="1143,4 1193,43 1143,82 1093,43" fill="var(--pink)" opacity="0.55"/>
    <polygon points="553,598 633,676 553,754 473,754 433,716" fill="var(--dot-red)" opacity="0.55"/>
    <polygon points="1108,650 1193,720 1193,754 1038,754 1038,720" fill="var(--pink)" opacity="0.55"/>
  </svg>

  <h1 class="headline">FOR SME BUSINESS ONLY!</h1>
  <div class="cta">CHAT WITH US!</div>
  <p class="offer">To get advice on how to apply<br>and defray up to <span class="highlight">80%</span> of business<br>laptop purchase cost!</p>
  <p class="terms">TERMS AND CONDITIONS APPLY</p>
</main>
</body>
</html>
```